Korvell Plant Services

We are a heavy diesel mechanical business with additional air con certificates, remapping engine rebuilt

Contact Information for Business Card

Company Name, Director Name, Managing Director, Contact details, email and website

Font styles to use
Serif
Script

```html
<!DOCTYPE html>
<html lang="en">
<head>
<meta charset="utf-8">
<title>Korvell Plant Services – Business Card</title>
<link href="https://fonts.googleapis.com/css2?family=Montserrat:wght@500;700;800&display=swap" rel="stylesheet">
<style>
  :root {
    --navy: #25237c;
    --ink: #141414;
    --paper: #ffffff;
    --backdrop: #e9e9ec;
    --machine-dark: #0d0d0d;
    --machine-mid: #2b2b2b;
  }
  * { box-sizing: border-box; margin: 0; padding: 0; }
  html, body {
    width: 1200px; height: 904px; overflow: hidden;
    background: var(--backdrop);
    font-family: "Montserrat", sans-serif;
  }
  .sheet {
    width: 1200px; height: 904px;
    display: flex; flex-direction: column;
    align-items: center; justify-content: center; gap: 36px;
  }
  .card {
    position: relative;
    width: 700px; height: 400px;
    background: var(--paper);
    box-shadow: 0 6px 18px rgba(0,0,0,.12);
    overflow: hidden;
  }
  /* Front */
  .card--front { display: flex; align-items: center; justify-content: center; }
  .brand { display: flex; align-items: center; gap: 14px; color: var(--navy); font-weight: 800; }
  .brand__dot { width: 22px; height: 22px; border-radius: 50%; background: var(--navy); flex: none; }
  .brand--large .brand__name { font-size: 34px; line-height: 1.1; }
  .brand--small .brand__name { font-size: 19px; line-height: 1.1; }
  .brand--small .brand__dot { width: 14px; height: 14px; }

  /* Back */
  .card--back .brand { position: absolute; left: 44px; top: 58px; }
  .person { position: absolute; left: 44px; top: 150px; }
  .person__name { color: var(--navy); font-weight: 800; font-size: 29px; letter-spacing: .5px; }
  .person__role { color: var(--ink); font-weight: 700; font-size: 14px; letter-spacing: .6px; margin-top: 4px; }
  .contact { position: absolute; left: 44px; top: 232px; list-style: none; }
  .contact__item { display: flex; align-items: center; gap: 12px; font-size: 17px; color: var(--ink); font-weight: 500; height: 28px; }
  .contact__icon { width: 17px; height: 17px; flex: none; }
  .address { position: absolute; left: 44px; top: 326px; font-size: 17px; line-height: 24px; color: var(--ink); font-weight: 500; }
  .machine-art {
    position: absolute; right: 26px; top: 22px;
    width: 215px; height: 330px;
    background: linear-gradient(180deg, var(--machine-mid), var(--machine-dark));
    border-radius: 6px;
  }
</style>
</head>
<body>
<main class="sheet">
  <section class="card card--front">
    <div class="brand brand--large">
      <span class="brand__dot"></span>
      <span class="brand__name">Korvell Plant Services</span>
    </div>
  </section>

  <section class="card card--back">
    <div class="brand brand--small">
      <span class="brand__dot"></span>
      <span class="brand__name">Korvell Plant Services</span>
    </div>

    <div class="person">
      <h1 class="person__name">ALDRIC PENROSE</h1>
      <p class="person__role">MANAGING DIRECTOR</p>
    </div>

    <ul class="contact">
      <li class="contact__item">
        <svg class="contact__icon" viewBox="0 0 24 24"><path fill="#25237c" d="M6.6 10.8a15.1 15.1 0 0 0 6.6 6.6l2.2-2.2c.3-.3.7-.4 1-.2 1.1.4 2.3.6 3.6.6.6 0 1 .4 1 1V20c0 .6-.4 1-1 1A17 17 0 0 1 3 4c0-.6.4-1 1-1h3.5c.6 0 1 .4 1 1 0 1.3.2 2.5.6 3.6.1.3 0 .7-.2 1z"/></svg>
        041-552 870 316
      </li>
      <li class="contact__item">
        <svg class="contact__icon" viewBox="0 0 24 24"><rect x="2" y="5" width="20" height="14" rx="1" fill="#25237c"/><path d="M3 6l9 7 9-7" stroke="#fff" stroke-width="1.6" fill="none"/></svg>
        hello@korvellplant.com
      </li>
      <li class="contact__item">
        <svg class="contact__icon" viewBox="0 0 24 24"><circle cx="12" cy="12" r="9.5" fill="none" stroke="#25237c" stroke-width="2"/><ellipse cx="12" cy="12" rx="4" ry="9.5" fill="none" stroke="#25237c" stroke-width="1.8"/><path d="M2.5 12h19M4 7h16M4 17h16" stroke="#25237c" stroke-width="1.6"/></svg>
        www.korvellplant.com
      </li>
    </ul>

    <p class="address">421, Address line goes here<br>45452, Country name</p>

    <div class="machine-art" role="img" aria-label="Black silhouette of an excavator arm and bucket"></div>
  </section>
</main>
</body>
</html>
```